Web design for a crypto donation landing page for wildlife protection projects

We are developing the landing page for the presale of a web3 project, which will collect cryptos to send them to wildlife protection projects.
Here some website we like:
https://www.tinyshareforcanopy.fr/
https://vorlq.io/
https://www.bramwild.io/
please, use the wireframe to know what blocks we want but we accept different template.
If possible, do the design on figma. Use 1 or 2 fonts max. Used green, blue and white, no more. Make a consistent system design by using the same font size for H1, H2, H3... and the same colors everywhere.
Number of Pages Required
1 page
Look and feel
Each slider illustrates characteristics of the customer's brand and the style your logo design should communicate.

```html
<!DOCTYPE html>
<html lang="en">
<head>
<meta charset="utf-8">
<title>Verdalia – Let's protect nature together</title>
<link rel="stylesheet" href="https://fonts.googleapis.com/css2?family=Heebo:wght@500;700;800&family=Roboto:wght@400&display=swap">
<style>
:root{
  --indigo:#26137a;
  --green:#79c943;
  --leaf:#3f9a2c;
  --white:#ffffff;
  --avatar:#f1f1f3;
}
*{margin:0;padding:0;box-sizing:border-box}
html,body{width:1200px;height:2635px;overflow:hidden;background:var(--white)}
body{position:relative;font-family:"Heebo",sans-serif;color:var(--indigo)}
.abs{position:absolute}
.hero{left:0;top:0;width:1200px;height:527px;background:linear-gradient(90deg,#f2f3f5 0%,#e4e7ea 100%)}
.hero-visual{left:430px;top:0;width:770px;height:527px;background:radial-gradient(circle at 62% 48%,#3f86b8 0%,#5aa35a 38%,#7dbb45 60%,rgba(228,231,234,0) 78%)}
.brand{left:70px;top:0;width:327px;height:182px;background:var(--indigo);border-radius:0 0 30px 30px;display:flex;align-items:center;justify-content:center}
.brand-name{font-weight:700;font-size:40px;color:var(--white);line-height:1}
.hero-title{left:40px;top:208px;width:395px;text-align:center;font-weight:800;font-size:46px;line-height:54px}
.hero-sub{left:40px;top:320px;width:395px;text-align:center;font-weight:700;font-size:30px;line-height:38px;color:var(--green)}
.box{border-radius:34px}
.box-green{background:var(--green)}
.box-indigo{background:var(--indigo)}
.intro{left:142px;top:586px;width:590px;height:342px;display:flex;align-items:center;justify-content:center;text-align:center;font-weight:700;font-size:30px;line-height:38px;padding:0 36px}
.buy{left:769px;top:586px;width:273px;height:342px;text-align:center;color:var(--green);font-weight:800}
.buy-big{font-size:64px;line-height:62px;margin-top:30px}
.buy-label{font-size:30px;line-height:32px}
.buy-count{font-size:62px;line-height:64px;margin-top:12px}
.buy-rate{font-size:30px;font-weight:700;line-height:36px}
.buy-btn{display:block;margin:20px auto 0;width:142px;height:51px;border-radius:8px;background:var(--green);color:var(--indigo);font-size:30px;line-height:51px;font-weight:800}
.h2{left:0;width:1200px;text-align:center;font-weight:800;font-size:46px;line-height:56px}
.h2 em{font-style:normal;color:var(--green)}
.step{top:1055px;width:273px;height:398px;text-align:center;color:var(--white);padding:16px 6px}
.step-kicker{color:var(--green);font-weight:700;font-size:30px;line-height:36px}
.step-big{color:var(--green);font-weight:800;font-size:64px;line-height:64px}
.step-text{font-family:"Roboto",sans-serif;font-size:21px;line-height:27px;margin-top:14px}
.step-text p+p{margin-top:27px}
.arrow{top:1130px;width:90px;height:240px}
.join-a{left:74px;top:1570px;width:509px;height:346px;display:flex;align-items:center;justify-content:center;text-align:center;font-weight:800;font-size:31px;line-height:38px}
.join-b{left:620px;top:1570px;width:508px;height:346px;padding:26px 34px;color:var(--white)}
.join-b h3{color:var(--green);text-align:center;font-weight:800;font-size:31px;line-height:38px;margin-bottom:22px}
.join-b li{font-family:"Roboto",sans-serif;font-size:21px;line-height:27px;list-style:none;position:relative;padding-left:18px;margin-bottom:16px}
.join-b li::before{content:"•";position:absolute;left:0}
.faq-row{left:185px;width:830px;display:flex;align-items:center;font-weight:700;font-size:31px;color:var(--green)}
.faq-row .line{flex:1;height:4px;background:var(--green);margin:14px 10px 0}
.member{top:2308px;width:260px;text-align:center;font-weight:700;font-size:20px;line-height:26px}
.avatar{width:174px;height:174px;border-radius:50%;background:var(--avatar);margin:0 auto 30px;display:flex;align-items:center;justify-content:center}
.member .name{color:var(--green)}
</style>
</head>
<body>
<div class="abs hero"></div>
<div class="abs hero-visual" role="img" aria-label="Moss-covered globe surrounded by plants, flowers and butterflies"></div>
<div class="abs brand"><span class="brand-name">Verdalia</span></div>
<h1 class="abs hero-title">Let's protect nature together</h1>
<p class="abs hero-sub">Donate tokens and help protect flora and fauna.</p>

<div class="abs box box-green intro"><p>Our platform allows you to add tokens of your choice to donate them to a nature protection project.<br><br>Your contribution will help finance concrete actions to preserve the environment.</p></div>
<div class="abs box box-indigo buy">
  <div class="buy-big">BUY</div>
  <div class="buy-label">TOKENS</div>
  <div class="buy-count">- 12 +</div>
  <div class="buy-rate">12 token = 30€</div>
  <span class="buy-btn">BUY</span>
</div>

<h2 class="abs h2" style="top:964px">How to protect nature with <em>Verdalia tokens?</em></h2>

<div class="abs box box-indigo step" style="left:70px">
  <div class="step-kicker">Buy tokens</div>
  <div class="step-big">HELP</div>
  <div class="step-text"><p>Tokens are digital assets that can be used to finance association projects.</p></div>
</div>
<svg class="abs arrow" style="left:343px" viewBox="0 0 90 240" role="img" aria-label="Arrow made of green leaves"><path d="M0 0 L90 120 L0 240 Z" fill="var(--leaf)"/></svg>
<div class="abs box box-indigo step" style="left:462px">
  <div class="step-big" style="margin-top:6px">VOTE</div>
  <div class="step-kicker" style="margin-top:-2px">for a project</div>
  <div class="step-text"><p>You can vote for a project of your choice.</p><p>The projects are proposed by associations and NGOs working to protect nature.</p></div>
</div>
<svg class="abs arrow" style="left:736px" viewBox="0 0 90 240" role="img" aria-label="Arrow made of green leaves"><path d="M0 0 L90 120 L0 240 Z" fill="var(--leaf)"/></svg>
<div class="abs box box-indigo step" style="left:855px">
  <div class="step-kicker" style="font-size:19px;margin-top:8px">The 1 association chosen</div>
  <div class="step-big" style="font-size:43px;line-height:46px;margin-top:10px">RECEIVES THE MONEY</div>
  <div class="step-text"><p>The project that received the most votes will receive the tokens.</p><p>The association will be able to use this money to finance its concrete actions to protect nature.</p></div>
</div>

<h2 class="abs h2" style="top:1491px">Join the community to <em>support nature protection</em></h2>

<div class="abs box box-green join-a"><p>NATURE IS IN DANGER,<br>WE MUST ACT TOGETHER.<br>JOIN THE COMMUNITY TO<br>SUPPORT NATURE<br>PROTECTION.</p></div>
<div class="abs box box-indigo join-b">
  <h3>BY JOINING THE COMMUNITY,<br>YOU WILL BE ABLE TO:</h3>
  <ul>
    <li>Follow the projects of associations working for protection of nature.</li>
    <li>Vote for the project of your choice and help finance its actions concretes.</li>
    <li>Be informed of the latest news on nature protection.</li>
  </ul>
</div>

<h2 class="abs h2" style="top:1952px">FAQ</h2>
<div class="abs faq-row" style="top:2009px">Question 1<span class="line"></span>IN</div>
<div class="abs faq-row" style="top:2085px">Question 2<span class="line"></span>IN</div>
<div class="abs faq-row" style="top:2161px">Question 3<span class="line"></span>IN</div>

<h2 class="abs h2" style="top:2233px">TEAM</h2>
<div class="abs member" style="left:121px">
  <div class="avatar"><svg width="86" height="110" viewBox="0 0 86 110" aria-hidden="true"><ellipse cx="43" cy="30" rx="22" ry="27" fill="var(--indigo)"/><path d="M0 110 V80 Q0 62 20 60 L43 72 L66 60 Q86 62 86 80 V110 Z" fill="var(--indigo)"/></svg></div>
  <div class="name">Delacroix<br>Bastien</div><div>Founder</div>
</div>
<div class="abs member" style="left:470px">
  <div class="avatar"><svg width="86" height="110" viewBox="0 0 86 110" aria-hidden="true"><ellipse cx="43" cy="32" rx="25" ry="30" fill="var(--indigo)"/><path d="M0 110 V80 Q0 62 20 60 L43 72 L66 60 Q86 62 86 80 V110 Z" fill="var(--indigo)"/></svg></div>
  <div class="name">Marchal<br>Elodie</div><div>Developpeuse<br>blockchain</div>
</div>
<div class="abs member" style="left:818px">
  <div class="avatar"><svg width="86" height="110" viewBox="0 0 86 110" aria-hidden="true"><ellipse cx="43" cy="32" rx="25" ry="30" fill="var(--indigo)"/><path d="M0 110 V80 Q0 62 20 60 L43 72 L66 60 Q86 62 86 80 V110 Z" fill="var(--indigo)"/></svg></div>
  <div class="name">Ferrand<br>Julie</div><div>Front-end developer</div>
</div>
</body>
</html>
```